Fashion Design Business Card

I need a new business card designed for a new fashion company. I have attached what I have currently designed. I want it more feminine looking, the logo needs to be gold. I want it simple, feminine and stylish. Please give me some different ideas with the fonts.
Updates

I need to send the design we currently have, as we have worked out the logo.
You also need all of our details
Industry/Entity Type
Fashion
Look and feel
Each slider illustrates characteristics of the customer's brand and the style your logo design should communicate.

```html
<!DOCTYPE html>
<html lang="en">
<head>
<meta charset="utf-8">
<title>Marina Vellard – Business Card</title>
<link rel="stylesheet" href="https://fonts.googleapis.com/css2?family=Josefin+Sans:wght@300;400&family=Cormorant+Garamond:ital,wght@1,400&display=swap">
<style>
  :root {
    --backdrop: #ebebeb;
    --card: #ffffff;
    --brand-gold: #c4a052;
    --ink: #3b3836;
    --ink-soft: #6a6562;
  }
  * { margin: 0; padding: 0; box-sizing: border-box; }
  html, body {
    width: 1200px;
    height: 900px;
    overflow: hidden;
    background: var(--backdrop);
    font-family: "Josefin Sans", sans-serif;
    font-weight: 300;
    color: var(--ink);
  }
  .stage { position: relative; width: 1200px; height: 900px; }
  .card {
    position: absolute;
    top: 298px;
    width: 484px;
    height: 304px;
    background: var(--card);
  }
  .card--front { left: 96px; }
  .card--back { left: 618px; }

  .brand-mark {
    position: absolute;
    left: 0; right: 0;
    text-align: center;
    color: var(--brand-gold);
    font-family: "Josefin Sans", sans-serif;
    font-weight: 300;
    line-height: 1;
    letter-spacing: 3px;
  }
  .card--front .brand-mark { top: 108px; font-size: 46px; }
  .card--back .brand-mark { top: 40px; font-size: 34px; }

  .holder-name {
    position: absolute;
    left: 0; right: 0;
    text-align: center;
    text-transform: uppercase;
    font-weight: 300;
    letter-spacing: 4px;
    word-spacing: 8px;
    line-height: 1;
  }
  .card--front .holder-name { top: 232px; font-size: 20px; }
  .card--back .holder-name { top: 150px; font-size: 18px; }

  .holder-role {
    position: absolute;
    top: 178px;
    left: 0; right: 0;
    text-align: center;
    font-family: "Cormorant Garamond", serif;
    font-style: italic;
    font-size: 21px;
    letter-spacing: 1px;
    line-height: 1;
    color: var(--ink-soft);
  }
  .divider {
    position: absolute;
    top: 219px;
    left: 0;
    width: 100%;
    height: 2px;
    background: var(--brand-gold);
  }
  .contact-list {
    position: absolute;
    top: 234px;
    left: 236px;
    list-style: none;
    font-size: 11px;
    font-weight: 400;
    line-height: 19px;
    letter-spacing: 0.5px;
    color: var(--ink-soft);
  }
  .contact-list .label { color: var(--brand-gold); margin-right: 5px; }
</style>
</head>
<body>
  <main class="stage">
    <section class="card card--front">
      <div class="brand-mark">Marina Vellard</div>
      <p class="holder-name">Marina Vellard</p>
    </section>

    <section class="card card--back">
      <div class="brand-mark">Marina Vellard</div>
      <p class="holder-name">Marina Vellard</p>
      <p class="holder-role">fashion designer</p>
      <div class="divider"></div>
      <ul class="contact-list">
        <li><span class="label">P.</span>0400 123 456</li>
        <li><span class="label">E.</span>marina@marinavellard.com</li>
        <li><span class="label">W.</span>www.marinavellard.com</li>
      </ul>
    </section>
  </main>
</body>
</html>
```